Business card design needed

I am a small start up business in the mortgage broking industry based in Sydney called 'nest2keys'. I will be providing residential mortgages to first home owners, investors and people looking to refinance. I would like to see designs that use the colors blue, black, and white - same as my logo (see logo design uploaded)

Target Market(s)

My target market is First Home Owners, property investors, and people looking to refinance. The loans I will be providing are for residential property only at this stage, and my clients will predominantly be in the 30-50yr age bracket.

Industry/Entity Type

Residential

Contact Information for Business Card

Owen Presley
Director/Mobile Mortgage Broker
nests2keys
PO BOX 2984
West Calder NSW 2175
Mb: 0471 286 904
email: owen@brickvaleplex.com.au

Requirements
Must have
• please use lower case for business name (i.e. nests2keys)

```html
<!DOCTYPE html>
<html lang="en">
<head>
<meta charset="utf-8">
<title>nests2keys – business card</title>
<link rel="stylesheet" href="https://fonts.googleapis.com/css2?family=Lato:wght@400;700&display=swap">
<style>
  :root {
    --stage: #e4e4e4;
    --card-black: #0c0c0c;
    --card-white: #ffffff;
    --brand-blue: #1fb1ea;
    --ink: #161616;
    --muted-ink: #3a3a3a;
    --pattern-dark: #1a1a1a;
    --photo-light: #eef0f1;
    --photo-mid: #dfe2e4;
  }
  * { box-sizing: border-box; margin: 0; padding: 0; }
  html, body { width: 1200px; height: 900px; overflow: hidden; }
  body {
    background: var(--stage);
    font-family: "Lato", "Helvetica Neue", Arial, sans-serif;
    position: relative;
  }
  .card {
    position: absolute;
    top: 291px;
    width: 520px;
    height: 318px;
    overflow: hidden;
    box-shadow: 0 6px 18px rgba(0,0,0,0.18);
  }

  /* Front face */
  .card-front {
    left: 60px;
    background: var(--card-black);
  }
  .front-texture {
    position: absolute;
    inset: 0;
    background: radial-gradient(ellipse at 50% 50%, var(--pattern-dark) 0%, var(--card-black) 75%);
  }
  .front-brand {
    position: absolute;
    left: 0; right: 0;
    top: 128px;
    text-align: center;
    color: var(--card-white);
    font-weight: 700;
    font-size: 40px;
    letter-spacing: 1px;
    line-height: 1;
  }
  .front-web {
    position: absolute;
    left: 0; right: 0;
    top: 182px;
    text-align: center;
    color: var(--card-white);
    font-weight: 400;
    font-size: 11px;
    letter-spacing: 0.3px;
  }

  /* Back face */
  .card-back {
    left: 620px;
    background: var(--card-white);
  }
  .back-photo {
    position: absolute;
    top: 0; right: 0;
    width: 340px;
    height: 262px;
    background: linear-gradient(90deg, rgba(255,255,255,1) 0%, var(--photo-light) 35%, var(--photo-mid) 100%);
    opacity: 0.8;
  }
  .back-brand {
    position: absolute;
    left: 30px;
    top: 72px;
    color: var(--ink);
    font-weight: 700;
    font-size: 26px;
    letter-spacing: 0.5px;
    line-height: 1;
  }
  .contact {
    position: absolute;
    left: 30px;
    top: 118px;
    color: var(--ink);
    font-size: 11px;
    line-height: 1.3;
  }
  .contact-name { font-size: 17px; font-weight: 400; line-height: 1.2; }
  .contact-role { font-size: 10.5px; color: var(--muted-ink); }
  .contact-company { font-size: 13px; font-weight: 700; margin-top: 6px; }
  .contact-address { font-size: 10.5px; color: var(--muted-ink); }
  .contact-lines { margin-top: 10px; display: grid; grid-template-columns: 52px auto; row-gap: 1px; font-size: 11px; }
  .contact-label { color: var(--brand-blue); }
  .back-band {
    position: absolute;
    left: 0; right: 0;
    top: 272px;
    height: 16px;
    background: var(--brand-blue);
  }
  .back-tab {
    position: absolute;
    right: 0;
    top: 246px;
    width: 22px;
    height: 26px;
    background: var(--card-black);
  }
  .back-square {
    position: absolute;
    right: 30px;
    top: 250px;
    width: 20px;
    height: 20px;
    background: var(--brand-blue);
  }
</style>
</head>
<body>
  <section class="card card-front" aria-label="Business card front">
    <div class="front-texture" role="img" aria-label="Faint repeating pattern on black"></div>
    <div class="front-brand">nests2keys</div>
    <div class="front-web">www.brickvaleplex.com.au</div>
  </section>

  <section class="card card-back" aria-label="Business card back">
    <div class="back-photo" role="img" aria-label="Faded photograph of a house facade"></div>
    <div class="back-brand">nests2keys</div>
    <div class="contact">
      <div class="contact-name">Owen Presley</div>
      <div class="contact-role">Director/Mobile Mortgage Broker</div>
      <div class="contact-company">nests2keys</div>
      <div class="contact-address">PO BOX 2984 West Calder NSW 2175</div>
      <div class="contact-lines">
        <span class="contact-label">mobile:</span><span>0471 286 904</span>
        <span class="contact-label">email:</span><span>owen@brickvaleplex.com.au</span>
        <span class="contact-label">web:</span><span>www.brickvaleplex.com.au</span>
      </div>
    </div>
    <div class="back-square"></div>
    <div class="back-tab"></div>
    <div class="back-band"></div>
  </section>
</body>
</html>
```